Tolbi Fund Map Tracker

Consumers track their three credit scores. I have sent an illustration after one update of their credit scores. Many consumers will have a dozen updates during one year. I would like to show a history of the last 24 months. Put together a design that is attractive and easy to look at and follow. I have updated some ideas for graphs (Apr 5, 2022)

Target Market(s)

Consumers tracking their credit scores

Coding

Coded - Design and coding required

Number of Pages Required

1 page

Colors
0054AA
0677BA
7BADD7
CADEEF
E8F1F8
00AB8E
00BBA5
67D7C9
C6EFE9
E9F9F6

Requirements
Must have
• Scores from 350 to 850 pon the left hand side - dates the credit scores were pulled at the bottom on the x axis
Nice to have
• 3 digit credit score for each of the three scores /

```html
<!DOCTYPE html>
<html lang="en">
<head>
<meta charset="utf-8">
<title>Tolbi Fund Map – Credit Score History</title>
<link href="https://fonts.googleapis.com/css2?family=Poppins:wght@400;500;700;800&family=Roboto:wght@400&display=swap" rel="stylesheet">
<style>
  :root{
    --header-bg:#f9f9f9;
    --page-bg:#ffffff;
    --brand-blue:#1d63c9;
    --title-blue:#0a0aef;
    --axis-green:#0a9a3a;
    --rule:#9a9a9a;
    --grid:#e9e9e9;
    --tick-text:#707070;
    --year-text:#9a9a9a;
    --legend-text:#7a7a7a;
    --bureau-a:#0000ff;
    --bureau-b:#3cb07a;
    --bureau-c:#e53b22;
    --line-a:#6b8de0;
    --dot-a:#c9d7f5;
    --line-b:#22cc88;
    --dot-b:#a6f2cf;
    --line-c:#f2222a;
    --dot-c:#f8a0a0;
  }
  *{margin:0;padding:0;box-sizing:border-box}
  html,body{width:1200px;height:891px;overflow:hidden;background:var(--page-bg)}
  .canvas{position:relative;width:1200px;height:891px;font-family:"Poppins",sans-serif}
  .site-header{position:absolute;left:0;top:0;width:1200px;height:99px;background:var(--header-bg)}
  .brand{position:absolute;left:89px;top:37px;display:flex;align-items:center;gap:10px}
  .brand-mark{width:30px;height:30px;background:var(--brand-blue);border-radius:3px}
  .brand-name{font-size:17px;font-weight:500;color:var(--brand-blue)}
  .page-title{position:absolute;left:84px;top:158px;font-size:26px;font-weight:800;color:var(--title-blue);letter-spacing:-0.3px}
  .title-rule{position:absolute;left:84px;top:196px;width:1033px;height:1.5px;background:var(--rule)}
  .chart{position:absolute;left:0;top:0}
  .tick{font-size:12px;fill:var(--tick-text)}
  .tick-month{font-size:10.5px;fill:var(--tick-text)}
  .tick-year{font-size:10.5px;font-weight:500;fill:var(--year-text)}
  .legend-label{font-family:"Roboto",sans-serif;font-size:19px;fill:var(--legend-text);letter-spacing:0.3px}
  .axis-title-y{font-size:20px;font-weight:800;fill:var(--title-blue)}
  .axis-title-x{font-size:21px;font-weight:700;fill:var(--axis-green)}
</style>
</head>
<body>
<div class="canvas">
  <header class="site-header">
    <div class="brand"><span class="brand-mark"></span><span class="brand-name">Tolbi Fund Map</span></div>
  </header>
  <h1 class="page-title">MY CREDIT SCORE HISTORY</h1>
  <div class="title-rule"></div>

  <svg class="chart" width="1200" height="891" viewBox="0 0 1200 891">
    <g class="legend">
      <rect x="655" y="238" width="41" height="24" fill="var(--bureau-a)"/>
      <text class="legend-label" x="705" y="256">KESTRAL</text>
      <rect x="800" y="238" width="42" height="24" fill="var(--bureau-b)"/>
      <text class="legend-label" x="852" y="256">BRIARLOW</text>
      <rect x="976" y="238" width="42" height="24" fill="var(--bureau-c)"/>
      <text class="legend-label" x="1027" y="256">QUILLON</text>
    </g>

    <g class="grid" stroke="var(--grid)" stroke-width="1">
      <line x1="166" y1="301" x2="1105" y2="301"/>
      <line x1="166" y1="345.1" x2="1105" y2="345.1"/>
      <line x1="166" y1="389.2" x2="1105" y2="389.2"/>
      <line x1="166" y1="433.3" x2="1105" y2="433.3"/>
      <line x1="166" y1="477.4" x2="1105" y2="477.4"/>
      <line x1="166" y1="521.5" x2="1105" y2="521.5"/>
      <line x1="166" y1="565.6" x2="1105" y2="565.6"/>
      <line x1="166" y1="609.7" x2="1105" y2="609.7"/>
      <line x1="166" y1="653.8" x2="1105" y2="653.8"/>
      <line x1="166" y1="697.9" x2="1105" y2="697.9"/>
      <line x1="166" y1="742" x2="1105" y2="742"/>
      <line x1="173" y1="301" x2="173" y2="750"/>
      <line x1="213.5" y1="301" x2="213.5" y2="750"/>
      <line x1="254" y1="301" x2="254" y2="750"/>
      <line x1="294.6" y1="301" x2="294.6" y2="750"/>
      <line x1="335.1" y1="301" x2="335.1" y2="750"/>
      <line x1="375.6" y1="301" x2="375.6" y2="750"/>
      <line x1="416.1" y1="301" x2="416.1" y2="750"/>
      <line x1="456.7" y1="301" x2="456.7" y2="750"/>
      <line x1="497.2" y1="301" x2="497.2" y2="750"/>
      <line x1="537.7" y1="301" x2="537.7" y2="750"/>
      <line x1="578.2" y1="301" x2="578.2" y2="750"/>
      <line x1="618.7" y1="301" x2="618.7" y2="750"/>
      <line x1="659.3" y1="301" x2="659.3" y2="750"/>
      <line x1="699.8" y1="301" x2="699.8" y2="750"/>
      <line x1="740.3" y1="301" x2="740.3" y2="750"/>
      <line x1="780.8" y1="301" x2="780.8" y2="750"/>
      <line x1="821.3" y1="301" x2="821.3" y2="750"/>
      <line x1="861.9" y1="301" x2="861.9" y2="750"/>
      <line x1="902.4" y1="301" x2="902.4" y2="750"/>
      <line x1="942.9" y1="301" x2="942.9" y2="750"/>
      <line x1="983.4" y1="301" x2="983.4" y2="750"/>
      <line x1="1023.9" y1="301" x2="1023.9" y2="750"/>
      <line x1="1064.5" y1="301" x2="1064.5" y2="750"/>
      <line x1="1105" y1="301" x2="1105" y2="750"/>
      <line x1="107" y1="811" x2="1110" y2="811"/>
    </g>

    <g class="tick" text-anchor="end">
      <text x="150" y="305">850</text>
      <text x="150" y="349">800</text>
      <text x="150" y="393">750</text>
      <text x="150" y="437">700</text>
      <text x="150" y="481">650</text>
      <text x="150" y="525">600</text>
      <text x="150" y="570">550</text>
      <text x="150" y="614">500</text>
      <text x="150" y="658">450</text>
      <text x="150" y="702">400</text>
      <text x="150" y="746">350</text>
    </g>

    <g class="tick-month" text-anchor="middle">
      <text x="173" y="770">MAY</text>
      <text x="213.5" y="770">JUN</text>
      <text x="254" y="770">JUL</text>
      <text x="294.6" y="770">AUG</text>
      <text x="335.1" y="770">SEP</text>
      <text x="375.6" y="770">OCT</text>
      <text x="416.1" y="770">NOV</text>
      <text x="456.7" y="770">DEC</text>
      <text x="497.2" y="770">JAN</text>
      <text x="537.7" y="770">FEB</text>
      <text x="578.2" y="770">MAR</text>
      <text x="618.7" y="770">APR</text>
      <text x="659.3" y="770">MAY</text>
      <text x="699.8" y="770">JUN</text>
      <text x="740.3" y="770">JUL</text>
      <text x="780.8" y="770">AUG</text>
      <text x="821.3" y="770">SEP</text>
      <text x="861.9" y="770">OCT</text>
      <text x="902.4" y="770">NOV</text>
      <text x="942.9" y="770">DEC</text>
      <text x="983.4" y="770">JAN</text>
      <text x="1023.9" y="770">FEB</text>
      <text x="1064.5" y="770">MAR</text>
      <text x="1105" y="770">APR</text>
    </g>
    <g class="tick-year" text-anchor="middle">
      <text x="173" y="788">2020</text>
      <text x="497.2" y="788">2021</text>
      <text x="983.4" y="788">2022</text>
    </g>

    <path fill="none" stroke="var(--line-a)" stroke-width="1.6"
      d="M173 715.5 C186.5 715.5 200 680.3 213.5 680.3 S240.5 645 254 645 S281.1 662.6 294.6 662.6 S321.6 689.1 335.1 689.1 S362.1 609.7 375.6 609.7 S402.6 530.3 416.1 530.3 S443.2 477.4 456.7 477.4 S483.7 415.7 497.2 415.7 S524.2 362.7 537.7 362.7 S564.7 336.3 578.2 336.3 S605.2 353.9 618.7 353.9 S645.8 398 659.3 398 S686.3 442.1 699.8 442.1 S726.8 477.4 740.3 477.4 S767.3 486.2 780.8 486.2 S807.8 468.6 821.3 468.6 S848.4 433.3 861.9 433.3 S888.9 398 902.4 398 S929.4 371.6 942.9 371.6 S969.9 345.1 983.4 345.1 S1010.4 415.7 1023.9 415.7 S1051 521.5 1064.5 521.5 S1091.5 556.8 1105 556.8"/>
    <path fill="none" stroke="var(--line-b)" stroke-width="1.6"
      d="M173 697.9 C186.5 697.9 200 671.4 213.5 671.4 S240.5 636.2 254 636.2 S281.1 653.8 294.6 653.8 S321.6 680.3 335.1 680.3 S362.1 689.1 375.6 689.1 S402.6 627.3 416.1 627.3 S443.2 556.8 456.7 556.8 S483.7 486.2 497.2 486.2 S524.2 442.1 537.7 442.1 S564.7 433.3 578.2 433.3 S605.2 442.1 618.7 442.1 S645.8 459.8 659.3 459.8 S686.3 477.4 699.8 477.4 S726.8 481.8 740.3 481.8 S767.3 477.4 780.8 477.4 S807.8 450.9 821.3 450.9 S848.4 415.7 861.9 415.7 S888.9 389.2 902.4 389.2 S929.4 362.7 942.9 362.7 S969.9 345.1 983.4 345.1 S1010.4 327.5 1023.9 327.5 S1051 318.6 1064.5 318.6 S1091.5 305.4 1105 305.4"/>
    <path fill="none" stroke="var(--line-c)" stroke-width="1.6"
      d="M173 609.7 C186.5 609.7 200 600.9 213.5 600.9 S240.5 592.1 254 592.1 S281.1 539.1 294.6 539.1 S321.6 486.2 335.1 486.2 S362.1 530.3 375.6 530.3 S402.6 592.1 416.1 592.1 S443.2 556.8 456.7 556.8 S483.7 450.9 497.2 450.9 S524.2 380.4 537.7 380.4 S564.7 327.5 578.2 327.5 S605.2 309.8 618.7 309.8 S645.8 314.2 659.3 314.2 S686.3 362.7 699.8 362.7 S726.8 503.9 740.3 503.9 S767.3 627.3 780.8 627.3 S807.8 680.3 821.3 680.3 S848.4 556.8 861.9 556.8 S888.9 433.3 902.4 433.3 S929.4 353.9 942.9 353.9 S969.9 336.3 983.4 336.3 S1010.4 318.6 1023.9 318.6 S1051 309.8 1064.5 309.8 S1091.5 380.4 1105 380.4"/>

    <g fill="var(--dot-a)" stroke="var(--line-a)" stroke-width="1.4">
      <circle cx="173" cy="715.5" r="4.8"/><circle cx="213.5" cy="680.3" r="4.8"/><circle cx="254" cy="645" r="4.8"/><circle cx="294.6" cy="662.6" r="4.8"/><circle cx="335.1" cy="689.1" r="4.8"/><circle cx="375.6" cy="609.7" r="4.8"/><circle cx="416.1" cy="530.3" r="4.8"/><circle cx="456.7" cy="477.4" r="4.8"/><circle cx="497.2" cy="415.7" r="4.8"/><circle cx="537.7" cy="362.7" r="4.8"/><circle cx="578.2" cy="336.3" r="4.8"/><circle cx="618.7" cy="353.9" r="4.8"/><circle cx="659.3" cy="398" r="4.8"/><circle cx="699.8" cy="442.1" r="4.8"/><circle cx="740.3" cy="477.4" r="4.8"/><circle cx="780.8" cy="486.2" r="4.8"/><circle cx="821.3" cy="468.6" r="4.8"/><circle cx="861.9" cy="433.3" r="4.8"/><circle cx="902.4" cy="398" r="4.8"/><circle cx="942.9" cy="371.6" r="4.8"/><circle cx="983.4" cy="345.1" r="4.8"/><circle cx="1023.9" cy="415.7" r="4.8"/><circle cx="1064.5" cy="521.5" r="4.8"/><circle cx="1105" cy="556.8" r="4.8"/>
    </g>
    <g fill="var(--dot-b)" stroke="var(--line-b)" stroke-width="1.4">
      <circle cx="173" cy="697.9" r="4.8"/><circle cx="213.5" cy="671.4" r="4.8"/><circle cx="254" cy="636.2" r="4.8"/><circle cx="294.6" cy="653.8" r="4.8"/><circle cx="335.1" cy="680.3" r="4.8"/><circle cx="375.6" cy="689.1" r="4.8"/><circle cx="416.1" cy="627.3" r="4.8"/><circle cx="456.7" cy="556.8" r="4.8"/><circle cx="497.2" cy="486.2" r="4.8"/><circle cx="537.7" cy="442.1" r="4.8"/><circle cx="578.2" cy="433.3" r="4.8"/><circle cx="618.7" cy="442.1" r="4.8"/><circle cx="659.3" cy="459.8" r="4.8"/><circle cx="699.8" cy="477.4" r="4.8"/><circle cx="740.3" cy="481.8" r="4.8"/><circle cx="780.8" cy="477.4" r="4.8"/><circle cx="821.3" cy="450.9" r="4.8"/><circle cx="861.9" cy="415.7" r="4.8"/><circle cx="902.4" cy="389.2" r="4.8"/><circle cx="942.9" cy="362.7" r="4.8"/><circle cx="983.4" cy="345.1" r="4.8"/><circle cx="1023.9" cy="327.5" r="4.8"/><circle cx="1064.5" cy="318.6" r="4.8"/><circle cx="1105" cy="305.4" r="4.8"/>
    </g>
    <g fill="var(--dot-c)" stroke="var(--line-c)" stroke-width="1.4">
      <circle cx="173" cy="609.7" r="4.8"/><circle cx="213.5" cy="600.9" r="4.8"/><circle cx="254" cy="592.1" r="4.8"/><circle cx="294.6" cy="539.1" r="4.8"/><circle cx="335.1" cy="486.2" r="4.8"/><circle cx="375.6" cy="530.3" r="4.8"/><circle cx="416.1" cy="592.1" r="4.8"/><circle cx="456.7" cy="556.8" r="4.8"/><circle cx="497.2" cy="450.9" r="4.8"/><circle cx="537.7" cy="380.4" r="4.8"/><circle cx="578.2" cy="327.5" r="4.8"/><circle cx="618.7" cy="309.8" r="4.8"/><circle cx="659.3" cy="314.2" r="4.8"/><circle cx="699.8" cy="362.7" r="4.8"/><circle cx="740.3" cy="503.9" r="4.8"/><circle cx="780.8" cy="627.3" r="4.8"/><circle cx="821.3" cy="680.3" r="4.8"/><circle cx="861.9" cy="556.8" r="4.8"/><circle cx="902.4" cy="433.3" r="4.8"/><circle cx="942.9" cy="353.9" r="4.8"/><circle cx="983.4" cy="336.3" r="4.8"/><circle cx="1023.9" cy="318.6" r="4.8"/><circle cx="1064.5" cy="309.8" r="4.8"/><circle cx="1105" cy="380.4" r="4.8"/>
    </g>

    <text class="axis-title-y" transform="translate(100 521) rotate(-90)" text-anchor="middle">Credit Score</text>
    <text class="axis-title-x" x="594" y="840" text-anchor="middle">Credit Pull Date</text>
  </svg>
</div>
</body>
</html>
```